Catchy Cards for Hospital

I run a rural hospital in Texas called Pellor Valley Hospital and am in need of contemporary business cards for all of my Department Heads. While our logo is somewhat simplistic, I don't have the option of changing it at this time, so anything to make the rest of the card present the appearance of a modern, professional healthcare facility would be great. Although the attached files are in black, our hospital colors are in a copper brown and black. I need to be able to change the name and title on the card so I can get cards printed for various department heads.

Target Market(s)

Referring physicians, large hospital systems, national organizations, state and federal government

Industry/Entity Type

Hospital

Contact Information for Business Card

Name Dale Hoskin
Title CEO

Phone: Main 325-555-0147 & Direct xxxxxx
Fax xxxxx
dale.hoskin@pellorvh.example
382 Wimble Street Box 415
Harrow Bend, Pellor Valley 76902

Font styles to use
Serif

Colors
f48340

Requirements
Must have
• Clean crisp lines and ability to modify names, titles and emails
• On the back "PellorValleyHospital.Example
Nice to have
• Needs to be in line with logo, which is a bit dated and not too appealing, but I'm hoping that the rest of the card can make up for that fact just a little bit.
• Hospital's colors are a copper brown, black and white
Should not have
• Shapes or anything distracting

```html
<!DOCTYPE html>
<html lang="en">
<head>
<meta charset="utf-8">
<title>Pellor Valley Hospital — Business Card</title>
<link rel="stylesheet" href="https://fonts.googleapis.com/css2?family=Lora:wght@400;500;700&display=swap">
<style>
  :root {
    --stage: #1b1b1b;
    --copper: #e97a36;
    --accent: #f48340;
    --paper: #eeece7;
    --ink: #141414;
    --white: #ffffff;
  }
  * { margin: 0; padding: 0; box-sizing: border-box; }
  html, body {
    width: 1200px;
    height: 1076px;
    overflow: hidden;
    background: var(--stage);
    font-family: "Lora", Georgia, serif;
  }
  .sheet {
    width: 1200px;
    height: 1076px;
    display: flex;
    flex-direction: column;
    align-items: center;
    justify-content: center;
    gap: 60px;
  }
  .card {
    position: relative;
    width: 760px;
    height: 437px;
    box-shadow: 0 6px 18px rgba(0,0,0,0.45);
  }
  .card-back {
    background: var(--copper);
    display: flex;
    align-items: center;
    justify-content: center;
  }
  .web-address {
    color: var(--white);
    font-size: 32px;
    letter-spacing: 0.5px;
  }
  .card-front {
    background: var(--paper);
    color: var(--ink);
  }
  .hospital-name {
    position: absolute;
    top: 44px;
    right: 40px;
    font-weight: 700;
    font-size: 34px;
    line-height: 1.08;
    color: var(--ink);
  }
  .contact {
    position: absolute;
    left: 36px;
    top: 200px;
  }
  .person-name {
    font-size: 28px;
    font-weight: 500;
    line-height: 1.2;
  }
  .person-title {
    font-size: 20px;
    color: var(--accent);
    line-height: 1.2;
  }
  .address {
    margin-top: 42px;
    font-size: 19px;
    line-height: 1.35;
  }
  .lines {
    margin-top: 16px;
    font-size: 19px;
    line-height: 1.35;
  }
  .label, .sep { color: var(--accent); }
</style>
</head>
<body>
  <main class="sheet">
    <section class="card card-back" aria-label="Card back">
      <p class="web-address">PellorValleyHospital.Example</p>
    </section>

    <section class="card card-front" aria-label="Card front">
      <p class="hospital-name">Pellor<br>Valley<br>Hospital</p>

      <div class="contact">
        <p class="person-name">Dale Hoskin</p>
        <p class="person-title">CEO</p>

        <p class="address">382 Wimble Street Box 415<br>Harrow Bend, Pellor Valley 76902</p>

        <p class="lines">
          <span class="label">Main:</span> 325-555-0147 <span class="sep">|</span>
          <span class="label">Direct:</span> 555-0182 <span class="sep">|</span>
          <span class="label">Fax:</span> 555-0193<br>
          <span class="label">Email:</span> dale.hoskin@pellorvh.example
        </p>
      </div>
    </section>
  </main>
</body>
</html>
```